Medical Waste Company with Logo

Need a business card design that targets office managers in the medical community. This card will be the front line for our sales team to market our services to the community. We would like to have email, phone number, website. Please use the logo attached to create a design that we would be proud of.

Target Market(s)

Medical Clients

Industry/Entity Type

Medical Supply

Contact Information for Business Card

Please use logo attached

Colors

Designer to choose colors to be used in the design.

Requirements
Must have
• Our logo (see attached file)
Nice to have
• Maybe a pop of some sort, raised..?

```html
<!DOCTYPE html>
<html lang="en">
<head>
<meta charset="utf-8">
<title>Northpeak Medical Waste – Business Card</title>
<link rel="stylesheet" href="https://fonts.googleapis.com/css2?family=Roboto+Slab:wght@400;500&display=swap">
<style>
  :root {
    --backdrop: #1c1c1c;
    --navy-deep: #0a3463;
    --navy-mid: #0f5a90;
    --brand-blue: #1d5fa3;
    --paper: #f1f1ef;
    --ink: #3a3a3a;
    --white: #ffffff;
  }
  * { margin: 0; padding: 0; box-sizing: border-box; }
  html, body {
    width: 1200px; height: 1200px; overflow: hidden;
    background: var(--backdrop);
    font-family: "Roboto Slab", Georgia, serif;
  }
  .sheet {
    position: relative; width: 1200px; height: 1200px;
    display: flex; flex-direction: column; align-items: center;
    justify-content: center; gap: 60px;
  }
  .card {
    position: relative; width: 840px; height: 480px;
    box-shadow: 0 10px 30px rgba(0,0,0,.45);
  }
  /* Front */
  .card--front {
    background: radial-gradient(ellipse at 50% 42%, var(--navy-mid) 0%, var(--navy-deep) 75%);
    display: flex; align-items: center; justify-content: center;
  }
  .brand-name {
    font-weight: 500; letter-spacing: 2px; text-transform: uppercase;
  }
  .card--front .brand-name { color: var(--white); font-size: 40px; }
  /* Back */
  .card--back { background: var(--paper); }
  .card--back .brand-name {
    position: absolute; right: 48px; top: 110px;
    color: var(--brand-blue); font-size: 30px;
  }
  .rule {
    position: absolute; left: 60px; right: 40px; top: 250px;
    height: 1.5px; background: var(--brand-blue);
  }
  .person { position: absolute; left: 60px; top: 170px; }
  .person__name {
    color: var(--brand-blue); font-size: 34px; font-weight: 500;
    letter-spacing: -0.5px;
  }
  .person__title { color: var(--ink); font-size: 17px; margin-top: 4px; margin-left: 28px; }
  .contacts {
    position: absolute; left: 88px; top: 282px; list-style: none;
  }
  .contacts li {
    display: flex; align-items: center; gap: 12px;
    color: var(--ink); font-size: 19px; line-height: 36px;
  }
  .contacts svg { width: 20px; height: 20px; fill: var(--brand-blue); flex: none; }
</style>
</head>
<body>
<main class="sheet">
  <section class="card card--front">
    <div class="brand-name">Northpeak Medical Waste</div>
  </section>

  <section class="card card--back">
    <div class="brand-name">Northpeak Medical Waste</div>
    <div class="person">
      <div class="person__name">Dr. JOHN DOE</div>
      <div class="person__title">Director</div>
    </div>
    <div class="rule"></div>
    <ul class="contacts">
      <li>
        <svg viewBox="0 0 24 24" aria-hidden="true"><path d="M3 9c0-3 4-5 9-5s9 2 9 5v2h-5V9c-2-.8-6-.8-8 0v2H3z"/><path d="M6 13h12l2 7H4z"/><circle cx="12" cy="16.5" r="2" fill="#f1f1ef"/></svg>
        1-234-567890
      </li>
      <li>
        <svg viewBox="0 0 24 24" aria-hidden="true"><circle cx="12" cy="12" r="10"/><path d="M2 12h20M12 2c3 3 3 17 0 20M12 2c-3 3-3 17 0 20" stroke="#f1f1ef" stroke-width="1.5" fill="none"/></svg>
        www.northpeakwaste.com
      </li>
      <li>
        <svg viewBox="0 0 24 24" aria-hidden="true"><rect x="2" y="5" width="20" height="14"/><path d="M2 5l10 8 10-8" stroke="#f1f1ef" stroke-width="1.5" fill="none"/></svg>
        john@northpeakwaste.com
      </li>
      <li>
        <svg viewBox="0 0 24 24" aria-hidden="true"><path d="M12 2a7 7 0 0 0-7 7c0 5 7 13 7 13s7-8 7-13a7 7 0 0 0-7-7z"/><circle cx="12" cy="9" r="2.5" fill="#f1f1ef"/></svg>
        Dummy city, Dummy Country Land
      </li>
    </ul>
  </section>
</main>
</body>
</html>
```